Steady Bloomwell HEMP Cannabis CBD tinctures

We need packaging for our line of CBD product label design based in Oakland Ca Brand is called 'Steady Bloomwell'. Our initial product is tincture to help people with pain with out the High effect of THC. I will be attaching og other company sample. The design should communicate slick look and relay health. Use the logo as way to color

Target Market(s)

CBD

Font styles to use
Serif
Decorative

Requirements
Must have
• Design that will make it stand out from the rest of the product on the shelve and be bright.
Nice to have
• The package must be able to stand out and not be dominated by Black color the green color must be the main color.
Should not have
• Be all black and get lost on the shelves

```html
<!DOCTYPE html>
<html lang="en">
<head>
<meta charset="utf-8">
<title>Steady Bloomwell HEMP Cannabis CBD Label</title>
<link href="https://fonts.googleapis.com/css2?family=Cabin:ital,wght@0,400;0,500;0,600;0,700;1,400&display=swap" rel="stylesheet">
<style>
  :root {
    --backdrop: #e4e4e4;
    --label-white: #ffffff;
    --ink: #1f1f1f;
    --brand-green: #3aaa6a;
    --band-light: #5cc48e;
    --band-mid: #2fa873;
    --band-deep: #1f9a63;
    --strip-green: #1e8f5a;
    --frame-line: #6cc596;
    --text-on-green: #e8f7ee;
  }
  * { margin: 0; padding: 0; box-sizing: border-box; }
  html, body {
    width: 1200px;
    height: 900px;
    overflow: hidden;
    background: var(--backdrop);
    font-family: "Cabin", sans-serif;
  }
  .stage {
    position: relative;
    width: 1200px;
    height: 900px;
  }
  .label {
    position: absolute;
    left: 300px;
    top: 40px;
    width: 600px;
    height: 820px;
    background: var(--label-white);
    overflow: hidden;
  }
  .label-band {
    position: absolute;
    left: 0;
    top: 445px;
    width: 600px;
    height: 320px;
    background: linear-gradient(160deg, var(--band-light) 0%, var(--band-mid) 45%, var(--band-deep) 100%);
  }
  .label-strip {
    position: absolute;
    left: 0;
    bottom: 0;
    width: 600px;
    height: 55px;
    background: var(--strip-green);
    display: flex;
    align-items: center;
    justify-content: center;
  }
  .volume {
    color: var(--text-on-green);
    font-size: 22px;
    letter-spacing: 1px;
  }
  .label-frame {
    position: absolute;
    left: 26px;
    top: 26px;
    width: 548px;
    height: 720px;
    border: 2px solid var(--frame-line);
  }
  .brand-lockup {
    position: absolute;
    left: 0;
    top: 190px;
    width: 600px;
    display: flex;
    align-items: center;
    justify-content: center;
    gap: 14px;
  }
  .brand-square {
    width: 26px;
    height: 26px;
    background: var(--brand-green);
  }
  .brand-name {
    color: var(--brand-green);
    font-weight: 600;
    font-size: 30px;
  }
  .product-title {
    position: absolute;
    left: 0;
    top: 358px;
    width: 600px;
    text-align: center;
    font-size: 54px;
    color: var(--ink);
    font-weight: 400;
    line-height: 1;
  }
  .product-title strong { font-weight: 700; }
  .product-type {
    position: absolute;
    left: 0;
    top: 450px;
    width: 600px;
    text-align: center;
    font-size: 44px;
    font-weight: 600;
    color: var(--label-white);
    line-height: 1;
  }
  .product-type .accent { color: #bfeed3; }
  .product-claim {
    position: absolute;
    left: 150px;
    top: 510px;
    width: 300px;
    text-align: center;
    font-size: 19px;
    font-style: italic;
    color: var(--text-on-green);
    line-height: 1.3;
  }
</style>
</head>
<body>
<main class="stage">
  <section class="label">
    <div class="label-band" role="img" aria-label="Faceted green geometric pattern"></div>
    <div class="label-strip"><span class="volume">30 ml</span></div>
    <div class="label-frame"></div>
    <div class="brand-lockup">
      <span class="brand-square"></span>
      <span class="brand-name">Steady Bloomwell</span>
    </div>
    <h1 class="product-title"><strong>Steady</strong> Bloomwell</h1>
    <p class="product-type"><span class="accent">HEMP</span> Cannabis CBD</p>
    <p class="product-claim">help people with pain without the high effect of THC</p>
  </section>
</main>
</body>
</html>
```